Web Design Project for SEARCH ENGINE !

We need a website design for torrents search engine.

The Website will be www.Qorvexa.com

Qorvexa is a a search engine for torrents.
Qorvexa search and index torrents results from all torrents sites.

We will need:
Logo
WebSite Design
slogen (optional)

we need only PSDs - no codded pages are needed !

Design to the following screen Size & resolution: 1024 x 768

***PLEASE DOWNLOAD ATTACHED FILE !

```html
<!DOCTYPE html>
<html lang="en">
<head>
<meta charset="utf-8">
<title>Qorvexa – Torrent Search</title>
<link rel="stylesheet" href="https://fonts.googleapis.com/css2?family=Gelasio:wght@400;700&family=Open+Sans:wght@400&display=swap">
<style>
  :root {
    --header-top: #00366a;
    --header-bottom: #1275b8;
    --header-rule: #c9d3dc;
    --panel-top: #ffffff;
    --panel-bottom: #98b1c8;
    --panel-edge: #5e7285;
    --field-border: #a9b4be;
    --button-top: #2a8fcf;
    --button-bottom: #0b5e99;
    --button-edge: #0a4b7c;
    --tagline: #0f3d6b;
    --body-text: #222222;
    --badge-fill: #eef1f4;
    --badge-edge: #c4cbd2;
    --mascot: #f2a340;
    --white: #ffffff;
  }
  * { box-sizing: border-box; margin: 0; padding: 0; }
  html, body { width: 1200px; height: 696px; overflow: hidden; background: var(--white); }
  body { position: relative; font-family: "Open Sans", Verdana, sans-serif; color: var(--body-text); }

  .site-header {
    position: absolute; left: 0; top: 0; width: 1200px; height: 132px;
    background: linear-gradient(to bottom, var(--header-top), var(--header-bottom));
    border-bottom: 3px solid var(--header-rule);
  }
  .brand {
    position: absolute; left: 52px; top: 26px;
    font-family: "Gelasio", Georgia, serif; font-weight: 700; font-size: 62px;
    color: var(--white); letter-spacing: 1px; line-height: 1;
  }
  .main-nav {
    position: absolute; right: 32px; top: 102px;
    font-family: "Gelasio", Georgia, serif; font-size: 16px; color: var(--white);
    display: flex; gap: 12px;
  }
  .main-nav a { color: var(--white); text-decoration: none; }

  .search-panel {
    position: absolute; left: 13px; top: 170px; width: 1174px; height: 162px;
    background: linear-gradient(to bottom, var(--panel-top) 0%, #e4ebf1 40%, var(--panel-bottom) 100%);
    border: 1px solid #c3ccd5; border-bottom: 1px solid var(--panel-edge);
    border-radius: 0 0 12px 12px;
  }
  .search-label {
    position: absolute; left: 25px; top: 12px;
    font-family: "Gelasio", Georgia, serif; font-size: 28px; color: #111;
  }
  .search-field {
    position: absolute; left: 23px; top: 58px; width: 944px; height: 59px;
    background: var(--white); border: 1px solid var(--field-border);
  }
  .search-button {
    position: absolute; left: 982px; top: 56px; width: 171px; height: 62px;
    background: linear-gradient(to bottom, var(--button-top), var(--button-bottom));
    border: 1px solid var(--button-edge); border-radius: 3px;
    font-family: "Gelasio", Georgia, serif; font-size: 28px; color: var(--white);
    display: flex; align-items: center; justify-content: center;
  }

  .tagline {
    position: absolute; left: 0; top: 358px; width: 1200px; text-align: center;
    font-family: "Gelasio", Georgia, serif; font-size: 21px; color: var(--tagline);
  }
  .share-row { position: absolute; left: 502px; top: 428px; display: flex; align-items: center; gap: 28px; }
  .share-badge { width: 104px; height: 29px; background: var(--badge-fill); border: 1px solid var(--badge-edge); border-radius: 3px; }
  .mascot { width: 26px; height: 28px; border-radius: 50%; background: radial-gradient(circle, #f8c57a, var(--mascot)); }

  .stats, .games {
    position: absolute; left: 0; width: 1200px; text-align: center; font-size: 17px; color: var(--body-text);
  }
  .stats { top: 488px; }
  .games { top: 530px; }

  .site-footer { position: absolute; left: 0; top: 593px; width: 1200px; text-align: center; font-size: 12.5px; color: #111; }
  .footer-links { display: flex; justify-content: center; gap: 12px; }
  .footer-links a { color: #111; text-decoration: none; }
  .copyright { margin-top: 4px; }
</style>
</head>
<body>
  <header class="site-header">
    <div class="brand">Qorvexa</div>
    <nav class="main-nav">
      <a href="#">Search</a><span>|</span>
      <a href="#">Seedrift</a><span>|</span>
      <a href="#">Profile</a><span>|</span>
      <a href="#">Help</a>
    </nav>
  </header>

  <section class="search-panel">
    <div class="search-label">Search</div>
    <div class="search-field"></div>
    <div class="search-button">Search</div>
  </section>

  <p class="tagline">Qorvexa is a FREE, FAST &amp;&nbsp; POWERFUL meta-search engine help you to get torrents from all over the world</p>

  <div class="share-row">
    <div class="share-badge" role="img" aria-label="Social share counter badge"></div>
    <div class="mascot" role="img" aria-label="Small cartoon mascot icon"></div>
  </div>

  <p class="stats">Indexing 15,448,499 active torrents from 49,102,720 pages on 33 domains</p>
  <p class="games">Find the best online games</p>

  <footer class="site-footer">
    <div class="footer-links">
      <a href="#">SSL</a><span>|</span>
      <a href="#">Torrent Plugin</a><span>|</span>
      <a href="#">Browser Search Plugin</a>
    </div>
    <div class="copyright">© 2011, All Right Reserved, qorvexa.com</div>
  </footer>
</body>
</html>
```